Business Card Design Project

I need a business card designed from scratch. I have an existing logo that I can upload in Illustrator for modification or redesign.

The Company is called Rank Harbor http://rankharbor.com.au and we provide Search Engine Optimization services to Australian businesses. The current logo signifies an increase in visitors, profits etc...

There are no restrictions as to the redesign - colours, style etc are all open to change.

Cards will be full colour and one sided printed at http://www.printlorvex.com.au so check their requirements for file format and sizes etc.

I will expect all original files upon completion of project.

Target Market(s)

Any business with a web site looking to improve their search engine rankings

Industry/Entity Type

Business

Requirements
Must have
• I like modern, sleek designs. Clean, not fussy, uncluttered.

```html
<!DOCTYPE html>
<html lang="en">
<head>
<meta charset="utf-8">
<title>Rank Harbor — Business Card</title>
<link rel="stylesheet" href="https://fonts.googleapis.com/css2?family=Arimo:wght@400;700&display=swap">
<style>
  :root {
    --backdrop: #8a8a8a;
    --card-deep: #1b1f96;
    --card-mid: #2634b8;
    --card-light: #3448cf;
    --brand-sky: #2f9be3;
    --accent-yellow: #f6e21a;
    --text-white: #ffffff;
    --ghost: rgba(70, 110, 230, 0.22);
  }
  * { margin: 0; padding: 0; box-sizing: border-box; }
  html, body {
    width: 1200px;
    height: 750px;
    overflow: hidden;
    background: var(--backdrop);
    font-family: "Arimo", Arial, sans-serif;
  }
  .canvas {
    width: 1200px;
    height: 750px;
    display: flex;
    align-items: center;
    justify-content: center;
  }
  .business-card {
    position: relative;
    width: 900px;
    height: 515px;
    overflow: hidden;
    color: var(--text-white);
    background:
      radial-gradient(ellipse at 55% 30%, var(--card-light) 0%, transparent 60%),
      linear-gradient(160deg, var(--card-mid) 0%, var(--card-deep) 100%);
    box-shadow: 0 12px 30px rgba(0, 0, 0, 0.35);
  }
  .ghost-name {
    position: absolute;
    left: 70px;
    top: 150px;
    font-weight: 700;
    font-size: 120px;
    line-height: 0.95;
    color: var(--ghost);
    letter-spacing: 2px;
    white-space: nowrap;
  }
  .accent-ring {
    position: absolute;
    right: 0;
    bottom: 0;
    width: 300px;
    height: 360px;
  }
  .brand {
    position: absolute;
    left: 330px;
    top: 52px;
    display: flex;
    align-items: center;
    gap: 16px;
  }
  .brand-dot {
    width: 34px;
    height: 34px;
    border-radius: 50%;
    background: var(--accent-yellow);
  }
  .brand-name {
    font-weight: 700;
    font-size: 48px;
    color: var(--brand-sky);
    letter-spacing: -0.5px;
  }
  .person {
    position: absolute;
    left: 0;
    right: 0;
    top: 160px;
    text-align: center;
    padding-left: 120px;
  }
  .person-name {
    font-size: 31px;
    font-weight: 400;
  }
  .person-role {
    margin-top: 6px;
    font-size: 19px;
  }
  .contacts {
    position: absolute;
    left: 60px;
    bottom: 48px;
    list-style: none;
    font-size: 23px;
  }
  .contact-item {
    display: flex;
    align-items: center;
    gap: 12px;
    height: 32px;
  }
  .contact-item.phone { padding-left: 64px; }
  .contact-icon { width: 22px; height: 22px; flex: none; }
</style>
</head>
<body>
<main class="canvas">
  <section class="business-card" aria-label="Rank Harbor business card">
    <div class="ghost-name" aria-hidden="true">RANK<br>HARBOR</div>

    <svg class="accent-ring" viewBox="0 0 300 360" aria-hidden="true">
      <circle cx="290" cy="250" r="200" fill="var(--accent-yellow)"/>
      <circle cx="300" cy="265" r="150" fill="var(--card-deep)"/>
    </svg>

    <div class="brand">
      <span class="brand-dot" aria-hidden="true"></span>
      <span class="brand-name">Rank Harbor</span>
    </div>

    <div class="person">
      <p class="person-name">Neil Varden</p>
      <p class="person-role">Internet Marketing Consultant</p>
    </div>

    <ul class="contacts">
      <li class="contact-item phone">
        <svg class="contact-icon" viewBox="0 0 24 24" aria-hidden="true">
          <path fill="#fff" d="M6.6 10.8a15.2 15.2 0 0 0 6.6 6.6l2.2-2.2c.3-.3.7-.4 1-.2 1.1.4 2.3.6 3.6.6.6 0 1 .4 1 1V20c0 .6-.4 1-1 1A17 17 0 0 1 3 4c0-.6.4-1 1-1h3.5c.6 0 1 .4 1 1 0 1.3.2 2.5.6 3.6.1.3 0 .7-.2 1z"/>
        </svg>
        <span>1300 482915</span>
      </li>
      <li class="contact-item email">
        <svg class="contact-icon" viewBox="0 0 24 24" aria-hidden="true">
          <rect x="2" y="5" width="20" height="14" fill="#fff"/>
          <path d="M2 5l10 8 10-8" fill="none" stroke="var(--card-deep)" stroke-width="1.6"/>
        </svg>
        <span>neil@rankharbor.com.au</span>
      </li>
      <li class="contact-item web">
        <svg class="contact-icon" viewBox="0 0 24 24" aria-hidden="true">
          <circle cx="12" cy="12" r="10" fill="var(--brand-sky)"/>
          <path d="M2 12h20M12 2c3 3 3 17 0 20M12 2c-3 3-3 17 0 20" fill="none" stroke="#fff" stroke-width="1.2"/>
        </svg>
        <span>www.rankharbor.com.au</span>
      </li>
    </ul>
  </section>
</main>
</body>
</html>
```